Pediatric Vision Care: Myopia Control Brochure

We are a pediatric eye care practice (ophthalmology and optometry). One of our services we offer for children is myopia control, which are strategies for slowing or stopping the progression of nearsightedness. This is a service we need to sell to parents because most insurance won't pay for it. There are different options we offer that can work well for kids in different situations: glasses with Corvane lenses, atropine eye drops, and/or special contact lenses. We need a brochure we can distribute to parents to let them know about this service that would encourage them to buy it for children who need it. Attached is our initial draft brochure created by our staff that provides text that we want to keep. The images and layout can change. We probably need at least one or two photos of kids on the brochure, because this is only something that works for children who are still growing, and the target audience is parents of 4-8 year old children.

Target Market(s)

Parents of 4-8 year old children

Font styles to use
Sans Serif

Requirements
Must have
• I'm uploading our company logo that should be included somewhere on the brochure. You can include contact information (web address, phone number) for our practice that is found on our website: http://www.brookhollowkidsvision.com/
Should not have
• This should not look childish. We need the impression to be friendly but professional, medical, expert.

```html
<!DOCTYPE html>
<html lang="en">
<head>
<meta charset="utf-8">
<title>Myopia Control Brochure – Brookhollow Kids Vision</title>
<link href="https://fonts.googleapis.com/css2?family=Arimo:wght@400;700&family=Oswald:wght@500;600&display=swap" rel="stylesheet">
<style>
  :root{
    --green:#8dc63f;
    --green-dark:#5a9a2e;
    --orange:#f7941d;
    --purple:#6b78bf;
    --yellow:#fdc82f;
    --grey:#d1d3d4;
    --trim:#ec6fb0;
    --ink:#111;
    --heading:"Oswald", "Arial Narrow", sans-serif;
    --body:"Arimo", Arial, sans-serif;
  }
  *{margin:0;padding:0;box-sizing:border-box}
  html,body{width:809px;height:1200px;overflow:hidden;background:#fff}
  body{font-family:var(--body);color:var(--ink)}
  .canvas{position:relative;width:809px;height:1200px;overflow:hidden}

  .spread{position:absolute;left:112px;width:582px;height:451px;border:1px solid var(--trim);display:flex;overflow:hidden}
  .spread--outside{top:90px}
  .spread--inside{top:628px}
  .panel{position:relative;width:194px;height:100%;flex:none}
  .panel + .panel{border-left:1px dashed var(--orange)}

  .heading{font-family:var(--heading);font-weight:600;font-variant:small-caps;letter-spacing:.2px;line-height:1}
  .body-copy{font-size:8.6px;line-height:1.18}
  .body-copy p + p{margin-top:7px}

  .brand{display:flex;align-items:center;gap:5px;font-family:var(--body);font-weight:700;color:var(--purple);white-space:nowrap}
  .brand__dot{border-radius:50%;background:var(--green);flex:none}

  /* outside spread */
  .photo{position:absolute;left:0;width:100%}
  .photo--reader{top:0;height:200px;background:linear-gradient(180deg,#8c6a5c 0%,#b58f80 40%,#e7d9d3 75%,#fff 100%)}
  .photo--eyewear{top:204px;height:150px;background:linear-gradient(180deg,#fff 0%,#d9c7c1 25%,#a88a80 55%,#d8c8c3 80%,#fff 100%)}
  .env{position:absolute;left:22px;right:20px;top:162px}
  .env .heading{font-size:17px;margin-bottom:5px}

  .contact{padding:10px 16px 0 18px;font-size:6.3px;line-height:1.5}
  .contact .heading{font-size:13px;text-align:center;margin-bottom:6px}
  .label{font-weight:700;font-size:8px;color:var(--purple)}
  .step{margin-top:7px}
  .step__num{display:inline-block;background:var(--purple);color:#fff;font-weight:700;padding:0 2px;margin-right:2px}
  .established{border:1px solid #b9bfe0;margin:6px -6px 0;padding:5px 8px}
  .established li{list-style:none;margin-top:7px;padding-left:6px;position:relative}
  .established li::before{content:"";position:absolute;left:0;top:2px;width:3px;height:3px;border-radius:50%;background:var(--purple)}
  .center{text-align:center}
  .phone-title{color:var(--green);font-weight:700;font-size:9.5px;margin-top:6px}
  .phone-line{font-weight:700;font-size:8px;margin-top:6px}
  .mail-title{color:var(--orange);font-weight:700;font-size:8px;margin-top:6px}
  .email-title{color:var(--purple);font-weight:700;font-size:8px;margin-top:5px}
  .chevron{position:absolute;left:0;bottom:0}
  .chevron .brand{position:absolute;left:50%;bottom:10px;transform:translateX(-50%);font-size:6px}

  .cover{padding:14px 22px 0 22px}
  .cover .brand{font-size:10px;margin:4px 0 0 8px}
  .cover .heading{font-size:20px;color:var(--purple);text-align:center;margin:16px 0 4px}
  .cover__lower{position:absolute;left:22px;right:20px;top:352px}
  .cover__lower strong{display:block;margin-top:7px;font-size:8.6px}

  .stripes{position:absolute}

  /* inside spread */
  .apex{position:absolute;left:0;top:0}
  .apex .brand{position:absolute;left:50%;top:10px;transform:translateX(-50%);font-size:7px}
  .option{position:absolute;left:23px;right:18px;top:44px}
  .option .heading{font-size:17px;line-height:1.08;height:52px;display:flex;align-items:flex-end;margin-bottom:12px}
  .option--glasses .heading{color:var(--green-dark)}
  .option--drops .heading{color:var(--orange);align-items:flex-end}
  .option--contacts .heading{color:var(--purple)}
  .shot{position:absolute;left:0;top:229px;width:100%;height:188px}
  .shot--glasses{background:linear-gradient(135deg,#f4f4f4 0%,#cfcfcf 40%,#444 70%,#e6e6e6 100%)}
  .shot--drops{background:radial-gradient(circle at 45% 70%,#6b7d90 0%,#b98a76 30%,#d9a48c 60%,#c4866e 100%)}
  .shot--contacts{background:linear-gradient(160deg,#9fd0ec 0%,#c3e4f5 50%,#8cc4e4 100%)}
  .base{position:absolute;left:0;bottom:0;width:100%;height:34px}
</style>
</head>
<body>
<main class="canvas">

  <!-- Outside spread -->
  <section class="spread spread--outside">
    <article class="panel panel--environment">
      <div class="photo photo--reader" role="img" aria-label="Photo of a young girl wearing red round glasses, resting her chin on her hand"></div>
      <div class="env">
        <h2 class="heading">Environmental Options:</h2>
        <div class="body-copy">
          <p>All myopic children can benefit from these lifestyle changes.</p>
          <p>It is important to get your child outdoors consistently. There is strong evidence that children who spend at least 2 hours a day outdoors are less likely to become myopic, and their myopia progresses slower than children who are outdoors less. Some studies show that increasing outdoor time by as few as 45 minutes a day is beneficial in reducing progression.</p>
          <p>There is some evidence that consistent use of screens, particularly held very close to the face, can worsen nearsightedness. We recommend limiting non- academic screen time and near work, and encourage your child to use the 20-20-20 rule. Every 20 minutes take a 20 second break to look at least 20 feet away.</p>
        </div>
      </div>
      <svg class="stripes" style="left:0;bottom:0" width="194" height="26" viewBox="0 0 194 26">
        <rect y="8" width="194" height="18" fill="var(--green)"/>
        <polygon points="0,0 30,0 24,8 0,8" fill="var(--purple)"/>
        <polygon points="36,0 62,0 56,8 30,8" fill="#fff"/>
        <polygon points="68,0 100,0 94,8 62,8" fill="var(--yellow)"/>
        <polygon points="106,0 138,0 132,8 100,8" fill="var(--orange)"/>
        <polygon points="144,0 176,0 170,8 138,8" fill="var(--purple)"/>
      </svg>
    </article>

    <article class="panel panel--contact">
      <div class="contact">
        <h2 class="heading">Contact Information</h2>
        <div class="label">Appointments</div>
        <div>If you are a new patient to our practice:</div>
        <p class="step"><span class="step__num">1</span>Fill out the new patient intake form and email it to us at appointments@brookhollowkidsvision.com.</p>
        <p class="step"><span class="step__num">2</span>We will call you to schedule after we receive your completed form. You're also welcome to contact us by one of the methods below to get scheduled once you have sent the form.</p>
        <div class="established">
          <div>If you are an established patient, you can schedule an appointment by either:</div>
          <ul>
            <li>Calling us at (555) 214-0300, and selecting option 1 to speak with a scheduler.</li>
            <li>Emailing us at appointments@brookhollowkidsvision.com. Please include a phone number where we can reach you if needed.</li>
            <li>Texting us at (555) 214-0311.</li>
          </ul>
        </div>
        <div class="center">
          <div class="phone-title">Telephone</div>
          <div class="phone-line">Voice: (555) 214-0300</div>
          <div class="phone-line">Text: (555) 214-0311</div>
          <div class="phone-line">Fax: (555) 214-0322</div>
          <div class="mail-title">Mailing Address</div>
          <div>Brookhollow Kids Vision<br>1280 Linden Park Road<br>Harbor Falls, ST 40210</div>
          <div class="email-title">Email</div>
          <div>Requests to schedule, cancel, or change an appointment should be sent to<br><strong>appointments@brookhollowkidsvision.com.</strong></div>
        </div>
      </div>
      <div class="chevron" style="width:194px;height:34px">
        <svg width="194" height="34" viewBox="0 0 194 34"><polygon points="0,14 97,0 194,14 194,34 0,34" fill="var(--grey)"/></svg>
        <div class="brand"><span class="brand__dot" style="width:5px;height:5px"></span>Brookhollow Kids Vision</div>
      </div>
    </article>

    <article class="panel panel--cover">
      <div class="cover">
        <div class="brand"><span class="brand__dot" style="width:9px;height:9px"></span>Brookhollow Kids Vision</div>
        <h1 class="heading">Myopia Control</h1>
        <div class="body-copy">
          <p>Myopia or nearsightedness causes blurry distance vision. Myopia is caused by the elongation of the eye, and progresses throughout childhood.</p>
          <p>Myopia is becoming increasingly common. More severe myopia and a higher glasses prescription is associated with a higher risk of eye problems involving the retina in adulthood, such as retinal problems and macular degeneration.</p>
        </div>
      </div>
      <div class="photo photo--eyewear" role="img" aria-label="Close-up photo of a child's eye behind clear-framed glasses"></div>
      <div class="cover__lower body-copy">
        <p>Myopia control is meant to slow the growth of the eye, keeping the glasses prescription as low as possible and reducing the risk of ocular disease in adulthood.</p>
        <strong>There are several treatment options.</strong>
      </div>
      <svg class="stripes" style="left:24px;top:422px" width="148" height="8" viewBox="0 0 148 8">
        <polygon points="0,0 38,0 33,8 0,8" fill="var(--purple)"/>
        <polygon points="40,0 74,0 69,8 35,8" fill="var(--green)"/>
        <polygon points="76,0 110,0 105,8 71,8" fill="var(--yellow)"/>
        <polygon points="112,0 148,0 148,8 107,8" fill="var(--orange)"/>
      </svg>
    </article>
  </section>

  <!-- Inside spread -->
  <section class="spread spread--inside">
    <svg class="apex" width="582" height="40" viewBox="0 0 582 40" style="z-index:0">
      <polygon points="60,0 522,0 290,40" fill="var(--grey)"/>
    </svg>
    <div class="apex" style="width:582px;z-index:2">
      <div class="brand"><span class="brand__dot" style="width:6px;height:6px"></span>Brookhollow Kids Vision</div>
    </div>

    <article class="panel">
      <div class="option option--glasses">
        <h2 class="heading">Lumetra Corvane<br>Glasses Lenses</h2>
        <div class="body-copy">
          <p>FDA market authorized Lumetra Corvane glasses lenses have been shown to slow myopia progression by about 50% in children aged 6-12.</p>
          <p>These lenses are a great treatment option because all your child needs to do is wear glasses. They look almost identical to ordinary glasses, but use specialized optics to signal the brain to slow the growth of myopic eyes.</p>
        </div>
      </div>
      <div class="shot shot--glasses" role="img" aria-label="Photo of black-framed children's glasses"></div>
      <svg class="base" viewBox="0 0 194 34" preserveAspectRatio="none">
        <rect y="8" width="194" height="26" fill="var(--green)"/>
        <polygon points="0,0 26,0 20,8 0,8" fill="var(--purple)"/>
        <polygon points="32,0 56,0 50,8 26,8" fill="var(--green)"/>
        <polygon points="62,0 96,0 90,8 56,8" fill="var(--yellow)"/>
        <polygon points="102,0 134,0 128,8 96,8" fill="var(--orange)"/>
        <polygon points="140,0 194,0 194,8 134,8" fill="var(--green)"/>
      </svg>
    </article>

    <article class="panel">
      <div class="option option--drops">
        <h2 class="heading">Low-Dose Atropine</h2>
        <div class="body-copy">
          <p>These eyedrops have been studied for over 20 years and have been shown to slow myopia progression by about 50% when used consistently.</p>
          <p>Low-dose atropine is simple to add to your daily routine. One drop is placed in each eye before bed each evening. These are ordered from a compounding pharmacy and mailed directly to your home.</p>
        </div>
      </div>
      <div class="shot shot--drops" role="img" aria-label="Photo of an eye drop being placed into an eye"></div>
      <svg class="base" viewBox="0 0 194 34" preserveAspectRatio="none">
        <rect y="8" width="194" height="26" fill="var(--orange)"/>
        <polygon points="0,0 34,0 28,8 0,8" fill="var(--yellow)"/>
        <polygon points="40,0 84,0 78,8 34,8" fill="var(--orange)"/>
        <polygon points="90,0 124,0 118,8 84,8" fill="var(--purple)"/>
        <polygon points="130,0 164,0 158,8 124,8" fill="var(--green)"/>
        <polygon points="170,0 194,0 194,8 164,8" fill="var(--yellow)"/>
      </svg>
    </article>

    <article class="panel">
      <div class="option option--contacts">
        <h2 class="heading">Specialty<br>Contact Lenses</h2>
        <div class="body-copy">
          <p>FDA-approved ClearPath lenses have been shown to slow myopia progression by about 50% in children aged 8-12.</p>
          <p>Contact lenses can be a great fit for many children, especially active children or those who do not enjoy wearing glasses. Many children as young as 7 or 8 are successful at wearing contacts.</p>
        </div>
      </div>
      <div class="shot shot--contacts" role="img" aria-label="Photo of a soft contact lens on a light blue background"></div>
      <svg class="base" viewBox="0 0 194 34" preserveAspectRatio="none">
        <rect y="8" width="194" height="26" fill="var(--purple)"/>
        <polygon points="0,0 38,0 32,8 0,8" fill="var(--orange)"/>
        <polygon points="44,0 76,0 70,8 38,8" fill="#9fd0ec"/>
        <polygon points="82,0 116,0 110,8 76,8" fill="var(--green)"/>
        <polygon points="122,0 156,0 150,8 116,8" fill="var(--yellow)"/>
        <polygon points="162,0 194,0 194,8 156,8" fill="var(--orange)"/>
      </svg>
    </article>
  </section>

</main>
</body>
</html>
```